Business Card Design - Law Firm

I need a business card design. I have attached a picture of the law firm's website and logo. The business card design should be consistent with those pictures. There should be a place for the employee name, employee job title, telephone number, facsimile number, address, website url, and email address for each employee.
Industry/Entity Type
Business

```html
<!DOCTYPE html>
<html lang="en">
<head>
<meta charset="utf-8">
<title>Marlowe Law — Business Cards</title>
<link rel="stylesheet" href="https://fonts.googleapis.com/css2?family=Libre+Baskerville&family=Open+Sans:wght@400&display=swap">
<style>
  :root {
    --page: #e9e9e9;
    --card: #3b3839;
    --gold: #b3a14b;
    --gold-soft: #c9b964;
    --shadow: rgba(0,0,0,0.28);
  }
  * { box-sizing: border-box; margin: 0; padding: 0; }
  html, body { width: 1200px; height: 899px; overflow: hidden; }
  body { background: var(--page); position: relative; font-family: "Open Sans", Arial, sans-serif; }

  .card {
    position: absolute;
    width: 560px;
    height: 320px;
    background: var(--card);
    border-radius: 22px;
    box-shadow: 0 6px 18px var(--shadow);
    overflow: hidden;
  }

  /* ---------- Contact side ---------- */
  .card--contact { left: 110px; top: 110px; }

  .brand {
    position: absolute;
    display: flex;
    align-items: center;
    gap: 14px;
  }
  .brand__mark { width: 26px; height: 26px; background: var(--gold); }
  .brand__text {
    font-family: "Libre Baskerville", Georgia, serif;
    color: var(--gold);
    line-height: 1;
  }
  .brand__name { display: block; }
  .brand__sub { display: block; text-align: center; letter-spacing: 2px; margin-top: 6px; }

  .card--contact .brand { left: 46px; top: 48px; }
  .card--contact .brand__name { font-size: 30px; }
  .card--contact .brand__sub { font-size: 9px; }

  .person { position: absolute; right: 40px; top: 56px; text-align: right; color: var(--gold); }
  .person__name { font-family: "Libre Baskerville", Georgia, serif; font-size: 22px; letter-spacing: 1px; }
  .person__title { font-size: 13px; margin-top: 2px; }

  .address { position: absolute; left: 46px; top: 170px; color: var(--gold); font-size: 11.5px; line-height: 26px; }
  .contacts { position: absolute; right: 46px; top: 170px; color: #e4e0d4; font-size: 11.5px; line-height: 26px; text-align: right; }

  .website { position: absolute; left: 0; right: 0; bottom: 30px; text-align: center; color: var(--gold); font-size: 14px; }

  .tab { position: absolute; width: 18px; height: 12px; background: var(--gold); }
  .tab--left { left: 0; clip-path: polygon(0 0, 70% 0, 100% 50%, 70% 100%, 0 100%); }
  .tab--right { right: 0; clip-path: polygon(30% 0, 100% 0, 100% 100%, 30% 100%, 0 50%); }

  /* ---------- Logo side ---------- */
  .card--logo { left: 560px; top: 480px; }
  .band { position: absolute; left: 0; right: 0; height: 30px; background: var(--gold); }
  .band--top { top: 0; }
  .band--bottom { bottom: 0; }

  .card--logo .brand { left: 50%; top: 50%; transform: translate(-50%, -50%); gap: 18px; }
  .card--logo .brand__mark { width: 34px; height: 34px; }
  .card--logo .brand__name { font-size: 42px; }
  .card--logo .brand__sub { font-size: 12px; }
</style>
</head>
<body>

  <section class="card card--contact" aria-label="Business card, contact side">
    <div class="brand">
      <span class="brand__mark"></span>
      <span class="brand__text">
        <span class="brand__name">Marlowe</span>
        <span class="brand__sub">LAW</span>
      </span>
    </div>

    <div class="person">
      <p class="person__name">YOUR NAME</p>
      <p class="person__title">Job Title</p>
    </div>

    <span class="tab tab--left" style="top:177px"></span>
    <span class="tab tab--left" style="top:229px"></span>
    <address class="address" style="font-style:normal">
      48 Alder Lane,<br>
      Suite 310 Halton,<br>
      Ohio 4410.
    </address>

    <span class="tab tab--right" style="top:177px"></span>
    <span class="tab tab--right" style="top:203px"></span>
    <span class="tab tab--right" style="top:229px"></span>
    <div class="contacts">
      <p>T : 123.456.7890</p>
      <p>F : 123.456.7890</p>
      <p>E : 123@marlowelaw.com</p>
    </div>

    <p class="website">www.marlowelaw.com</p>
  </section>

  <section class="card card--logo" aria-label="Business card, logo side">
    <span class="band band--top"></span>
    <div class="brand">
      <span class="brand__mark"></span>
      <span class="brand__text">
        <span class="brand__name">Marlowe</span>
        <span class="brand__sub">LAW</span>
      </span>
    </div>
    <span class="band band--bottom"></span>
  </section>

</body>
</html>
```